Colorful Live Music Concert Poster for Tin Harbor

Looking for a portrait oriented "poster" promoting the band's upcoming show at Marlow Lounge on Sunday, 3/22 at 8 pm, and social version (square format for Instagram). <br/><br/>Copy:<br/>Tin Harbor<br/>with The Pale Wires<br/><br/>Marlow Lounge <br/>Sunday, March 22<br/>8 pm<br/><br/>Poster must be consistent with band's overall branding seen on www.tinharborband.example and it's Tunevault page at https://music.example.com/artist/7QxRtaWpLeNmVcz2Ks9DuB?si=381fkTsYpWmaGHeLoRqdXC <br/><br/>BUT, we wouldn't mind taking in a slightly updated direction. A good example is the cover for our recent single Glad Today, which is consistent in theme and color palette while updating the design and color at the same time. <br/><br/>The attached files include some band logo art as well as examples of posters done for prior shows. <br/><br/>The posters need not include photos of the band, but if you are so inclined, we've uploaded some selects as well.<br/><br/>Thank you. <br/><br/>Wendell<br/>Tin Harbor

```html
<!DOCTYPE html>
<html lang="en">
<head>
<meta charset="utf-8">
<title>Tin Harbor with The Pale Wires – Marlow Lounge</title>
<link rel="stylesheet" href="https://fonts.googleapis.com/css2?family=Josefin+Sans:wght@300;400;600&display=swap">
<style>
  :root {
    --teal: #11a5a9;
    --white: #ffffff;
    --stone: #8fb3bb;
    --mist: #b6d6d7;
    --slate: #7a9bb0;
    --amber: #f8ae3b;
    --rose: #f18fab;
    --brick-warm: #e6c47a;
    --brick-cool: #6fc3c0;
  }
  html, body {
    margin: 0;
    padding: 0;
    overflow: hidden;
    background: var(--teal);
  }
  .poster {
    position: relative;
    width: 1200px;
    height: 1200px;
    background: var(--teal);
    overflow: hidden;
    font-family: "Josefin Sans", sans-serif;
    color: var(--white);
  }
  .artwork {
    position: absolute;
    left: 140px;
    top: 94px;
    width: 922px;
    height: 626px;
    background:
      radial-gradient(ellipse 34% 46% at 50% 62%, rgba(248, 174, 59, 0.85) 0%, rgba(248, 174, 59, 0) 100%),
      radial-gradient(ellipse 30% 40% at 84% 86%, rgba(241, 143, 171, 0.55) 0%, rgba(241, 143, 171, 0) 100%),
      radial-gradient(ellipse 40% 60% at 26% 62%, rgba(143, 179, 187, 0.9) 0%, rgba(143, 179, 187, 0) 100%),
      radial-gradient(ellipse 40% 60% at 76% 52%, rgba(182, 214, 215, 0.9) 0%, rgba(182, 214, 215, 0) 100%);
  }
  .sunburst {
    position: absolute;
    left: 918px;
    top: 26px;
    width: 184px;
    height: 184px;
    border-radius: 50%;
    background: radial-gradient(circle, rgba(255, 255, 255, 0.35) 0%, rgba(255, 255, 255, 0) 70%);
  }
  .divider {
    position: absolute;
    left: 74px;
    top: 721px;
    width: 1052px;
    height: 2px;
    background: var(--white);
  }
  .headliner {
    position: absolute;
    top: 252px;
    left: 0;
    width: 1200px;
    margin: 0;
    text-align: center;
    font-weight: 400;
    font-size: 136px;
    letter-spacing: 22px;
    text-indent: 22px;
    line-height: 1;
    color: transparent;
    -webkit-text-stroke: 2px var(--white);
    background: linear-gradient(180deg, var(--white) 0%, var(--white) 50%, transparent 50%, transparent 100%);
    -webkit-background-clip: text;
    background-clip: text;
  }
  .support {
    position: absolute;
    top: 744px;
    left: 0;
    width: 1200px;
    margin: 0;
    text-align: center;
    font-weight: 600;
    font-size: 76px;
    letter-spacing: 3px;
    line-height: 1;
    color: transparent;
    -webkit-text-stroke: 2px var(--white);
  }
  .band-photo {
    position: absolute;
    left: 80px;
    top: 830px;
    width: 346px;
    height: 341px;
    background: linear-gradient(180deg, var(--brick-warm) 0%, var(--brick-warm) 45%, var(--brick-cool) 60%, var(--brick-cool) 100%);
  }
  .details {
    position: absolute;
    left: 452px;
    top: 872px;
    width: 700px;
    margin: 0;
    text-align: center;
    font-weight: 300;
    font-size: 62px;
    letter-spacing: 3px;
    line-height: 86px;
  }
  .details span { display: block; }
  .socials {
    position: absolute;
    left: 496px;
    top: 1136px;
    display: flex;
    gap: 26px;
    font-size: 17px;
    font-weight: 400;
    align-items: center;
  }
  .social {
    display: flex;
    align-items: center;
    gap: 8px;
  }
  .social-dot {
    width: 34px;
    height: 34px;
    border-radius: 50%;
    background: var(--white);
  }
</style>
</head>
<body>
  <main class="poster">
    <div class="artwork" role="img" aria-label="Abstract composition of overlapping triangles in grey, pale blue, amber and pink"></div>
    <div class="sunburst" role="img" aria-label="Thin-line sunburst ornament"></div>
    <div class="divider"></div>

    <h1 class="headliner">TIN HARBOR</h1>
    <h2 class="support">WITH THE PALE WIRES</h2>

    <div class="band-photo" role="img" aria-label="Photo of the two band members leaning against a yellow and teal brick wall"></div>

    <p class="details">
      <span>MARLOW LOUNGE</span>
      <span>ON SUNDAY</span>
      <span>MARCH 22 AT 8 PM</span>
    </p>

    <div class="socials">
      <div class="social"><span class="social-dot"></span><span>@tinharborband</span></div>
      <div class="social"><span class="social-dot"></span><span>@tinharborband</span></div>
      <div class="social"><span class="social-dot"></span><span>/tinharborband</span></div>
    </div>
  </main>
</body>
</html>
```